my website is tabellepiece.com. (brand name is ta belle pièce) This is just a template that i have choose for. The content and the pictures are not about my business just the template.
I would like to have 4 pages for now. 1 homepage, which will be an overview for all pages, it is right now in this way. It will directly highlight my story. My website will tell an exclusive story about details which makes the difference and will make people happy with very small things. It will be art related but very stylish as well. I also want to have a event agenda on my homepage where people can see where my next event is. Page 2 my blog, where I will write weekly about mindset, lifestyle and details. Inspiration place for people who are looking for unique and exclusive approaches in life. Page 3 shop, where I will sell my stuff which is handmade and unique, it will be limited edition stuff. Mostly I will make the designs from marbling art, which I am a teacher for. (https://www.vidorastream.com/watch?v=Kq7TbWm2Xa) check this video out for more. Page 4 is book page. Here people will be able to book private or group classes for marbling art (check the video). I have already a community of more than 500 people on join ring, which will be my public as well. I wanna implement the join ring button on this page as well. to be able to track.

This is about my website. I also need a logo for my brand, which will suit my website and my goals.

I can also give you a reference website, which really like as structure and style;
https://www.brightmorrowco.com/products/the-daybook-organizer?ref=Xp4RtLm8QzVw2NbKc7HsJd9FgTy3MvEqBa6WnUoZr1LkPxYhGiCe5DsAtQfVbNj0HmRwKyXo8LcTpZaEsUv2GqDnIwMb

ta belle pièce

4 page

• I can also give you a reference website, which really like as structure and style;
• https://www.brightmorrowco.com/products/the-daybook-organizer?ref=Xp4RtLm8QzVw2NbKc7HsJd9FgTy3MvEqBa6WnUoZr1LkPxYhGiCe5DsAtQfVbNj0HmRwKyXo8LcTpZaEsUv2GqDnIwMb

```html
<!DOCTYPE html>
<html lang="en">
<head>
<meta charset="utf-8">
<title>Ta Belle Pièce</title>
<link href="https://fonts.googleapis.com/css2?family=Kaushan+Script&family=Lato:wght@400;700;900&display=swap" rel="stylesheet">
<style>
:root{
  --red:#d8322a;
  --red-dark:#b92720;
  --ink:#222222;
  --body:#555555;
  --grey-band:#e8e8e8;
  --footer:#2a2a2a;
  --white:#ffffff;
  --line:#333333;
}
*{box-sizing:border-box;margin:0;padding:0}
html,body{width:1200px;height:3814px;overflow:hidden}
body{position:relative;background:var(--white);font-family:'Lato',sans-serif;color:var(--ink)}
.abs{position:absolute}
.topbar{left:0;top:0;width:1200px;height:25px;background:var(--red);color:var(--white);font-size:11px;font-weight:700;line-height:25px;padding:0 122px}
.topbar .social{position:absolute;right:122px;top:7px;display:flex;gap:9px}
.topbar .social span{width:11px;height:11px;border-radius:50%;background:var(--white);display:block}
.header{left:0;top:25px;width:1200px;height:148px;background:var(--white)}
.brand{position:absolute;left:122px;top:50px;display:flex;align-items:center;gap:16px}
.brand-dot{width:66px;height:66px;border-radius:50%;background:var(--red)}
.brand-name{font-size:38px;font-weight:900;color:var(--red)}
.nav-icons{position:absolute;right:122px;top:58px;display:flex;gap:22px}
.hero{left:0;top:173px;width:1200px;height:569px;background:linear-gradient(180deg,#3a2f2b 0%,#5a3a35 35%,#7d4740 70%,#6a3d39 100%)}
.hero-copy{left:0;top:258px;width:1200px;text-align:center;color:var(--white)}
.hero-title{font-family:'Kaushan Script',cursive;font-size:40px}
.hero-text{font-size:14px;font-weight:700;line-height:18px;margin-top:14px}
.btn{display:inline-block;background:var(--red);color:var(--white);font-size:13px;font-weight:700;text-transform:uppercase;text-align:center}
.hero .btn,.hero-btn{left:526px;top:567px;width:158px;height:43px;line-height:43px;font-size:15px}
.photo{display:block}
.section-title{font-family:'Kaushan Script',cursive;color:var(--red);font-size:32px;line-height:40px}
.title-rule{width:52px;height:3px;background:var(--line);margin:10px 0 18px}
.lead{font-size:15px;font-weight:900;line-height:20px;color:var(--ink)}
.copy{font-size:13px;line-height:17px;color:var(--body)}
.block-btn{width:135px;height:40px;line-height:40px;font-size:12px}
.arrows{display:flex;gap:3px}
.arrows span{width:32px;height:33px;display:flex;align-items:center;justify-content:center}
.arrows .prev{background:var(--ink)}
.arrows .next{background:var(--red)}
.meta{display:flex;gap:18px;font-size:9px;color:#888;text-transform:uppercase;letter-spacing:.5px}
.price{font-size:24px;font-weight:700;color:var(--ink)}
.stars{display:flex;align-items:center;gap:8px;font-size:11px;color:var(--body)}
.stars b{color:#f2b01e;font-size:15px;letter-spacing:1px}
.buy{display:flex;align-items:center;gap:6px;font-size:12px}
.qty{width:22px;height:22px;border:1px solid #aaa;text-align:center;line-height:20px;font-size:11px}
.field{position:absolute;border:2px solid var(--line);font-size:12px;padding:6px 8px;color:var(--ink);background:var(--white)}
.info-band{left:0;top:3218px;width:1200px;height:318px;background:var(--grey-band)}
.info{position:absolute;top:92px;width:240px;text-align:center}
.info .circle{width:92px;height:92px;border-radius:50%;background:var(--red);margin:0 auto 30px;display:flex;align-items:center;justify-content:center}
.info h4{font-size:14px;font-weight:700;letter-spacing:1px;color:var(--ink)}
.info p{font-size:14px;margin-top:10px;color:var(--ink)}
.newsletter{left:0;top:3536px;width:1200px;height:236px;background:linear-gradient(180deg,var(--red) 0%,var(--red-dark) 100%);color:var(--white);text-align:center}
.newsletter h3{font-size:26px;font-weight:900;letter-spacing:2px;margin-top:60px}
.newsletter h5{font-size:14px;font-weight:700;letter-spacing:1.5px;margin-top:4px}
.subscribe{position:absolute;left:364px;top:140px;width:508px;height:40px;background:var(--white);display:flex;align-items:center;padding:0 6px 0 14px}
.subscribe span{flex:1;text-align:left;color:#888;font-size:10px}
.subscribe b{background:var(--red);color:var(--white);font-size:11px;letter-spacing:1px;width:120px;height:22px;line-height:22px}
.footer{left:0;top:3772px;width:1200px;height:42px;background:var(--footer);color:var(--white);font-size:12px;font-weight:700;line-height:42px;padding:0 122px}
.footer .social{position:absolute;right:122px;top:15px;display:flex;gap:12px}
.footer .social span{width:12px;height:12px;border-radius:50%;background:var(--white);display:block}
</style>
</head>
<body>

<div class="abs topbar">info@tabellepiece.com
  <div class="social"><span></span><span></span><span></span><span></span><span></span></div>
</div>

<header class="abs header">
  <div class="brand"><div class="brand-dot"></div><div class="brand-name">Ta Belle Pièce</div></div>
  <div class="nav-icons">
    <svg width="26" height="26" viewBox="0 0 26 26" fill="none" stroke="#222" stroke-width="2"><circle cx="13" cy="8" r="6"/><path d="M2 25c1-7 6-10 11-10s10 3 11 10"/></svg>
    <svg width="28" height="26" viewBox="0 0 28 26" fill="none" stroke="#222" stroke-width="2"><path d="M1 3h5l4 14h13l3-10H8"/><circle cx="11" cy="22" r="2"/><circle cx="21" cy="22" r="2"/></svg>
    <svg width="24" height="26" viewBox="0 0 24 26" stroke="#222" stroke-width="2.5"><path d="M1 6h22M1 13h22M1 20h22"/></svg>
  </div>
</header>

<section class="abs hero" role="img" aria-label="Marbling tray with floating paint patterns and jars of colour on a workshop table"></section>
<div class="abs hero-copy">
  <div class="hero-title">Ta Belle Pièce</div>
  <p class="hero-text">Lorem Ipsum is simply dummy text of the printing<br>and typesetting industry.</p>
</div>
<div class="abs btn hero-btn">Read More</div>

<!-- Story -->
<div class="abs photo" style="left:122px;top:816px;width:452px;height:498px;background:linear-gradient(160deg,#c58f8a,#9d6461 55%,#7b4b49)" role="img" aria-label="Hand drawing a stylus through pink marbling paint"></div>
<article class="abs" style="left:633px;top:878px;width:450px">
  <h2 class="section-title">My Story</h2>
  <div class="title-rule"></div>
  <p class="lead">Lorem Ipsum is simply dummy text of the printing and typesetting industry.</p>
  <p class="copy" style="margin-top:14px">ta belle pièce is a leading Online Store. We provide an unparalleled selection of the very best quality products, an easy and comfortable shopping experience, expedited shipping offers, and exceptional customer service. Check out our collection of new arrivals, best sellers, and clearance items today.</p>
  <div class="btn block-btn" style="margin-top:24px">Read More</div>
</article>

<!-- Blog -->
<article class="abs" style="left:120px;top:1462px;width:452px">
  <h2 class="section-title">Blog</h2>
  <div class="title-rule"></div>
  <p class="lead">Lorem Ipsum is simply dummy text of the printing and typesetting industry.</p>
  <div class="meta" style="margin:16px 0 14px"><span>10:40 AM</span><span>Posted by Atelier Notes</span><span>0 Comments</span></div>
  <p class="copy">ta belle pièce is a leading Online Store. We provide an unparalleled selection of the very best quality products, an easy and comfortable shopping experience, expedited shipping offers, and exceptional customer service. Check out our collection of new arrivals, best sellers, and clearance items today.</p>
  <div class="btn block-btn" style="margin-top:24px">Read More</div>
</article>
<div class="abs arrows" style="left:507px;top:1863px">
  <span class="prev"><svg width="10" height="14" viewBox="0 0 10 14"><path d="M8 1L2 7l6 6" stroke="#fff" stroke-width="2.5" fill="none"/></svg></span>
  <span class="next"><svg width="10" height="14" viewBox="0 0 10 14"><path d="M2 1l6 6-6 6" stroke="#fff" stroke-width="2.5" fill="none"/></svg></span>
</div>
<div class="abs photo" style="left:630px;top:1398px;width:453px;height:498px;background:linear-gradient(170deg,#6f7a3a,#5a3f6a 50%,#8b6a9a 75%,#4a3552)" role="img" aria-label="Paint brushes resting in a marbling bath of purple and green colour"></div>

<!-- Shop -->
<div class="abs photo" style="left:122px;top:1983px;width:452px;height:432px;background:linear-gradient(135deg,#8fc7cf,#9aa85a 45%,#e889a0 70%,#8fc7cf)" role="img" aria-label="Marbled paper with pink flower shapes on turquoise"></div>
<div class="abs" style="left:122px;top:2428px;width:452px;height:106px;display:flex;gap:8px">
  <div style="flex:1;background:linear-gradient(135deg,#8fc7cf,#a3ad60)" role="img" aria-label="Marbled paper thumbnail"></div>
  <div style="flex:1;background:linear-gradient(135deg,#d96a54,#8fc7cf)" role="img" aria-label="Marbled paper thumbnail"></div>
  <div style="flex:1;background:linear-gradient(135deg,#a3ad60,#e889a0)" role="img" aria-label="Marbled paper thumbnail"></div>
  <div style="flex:1;background:linear-gradient(135deg,#e889a0,#8fc7cf)" role="img" aria-label="Marbled paper thumbnail"></div>
</div>
<article class="abs" style="left:630px;top:2047px;width:453px">
  <h2 class="section-title">My Stuff</h2>
  <div class="title-rule"></div>
  <p class="lead">Lorem Ipsum is simply dummy text of the printing and typesetting industry.</p>
  <p class="price" style="margin-top:12px">$500.00USD</p>
  <div class="stars" style="margin-top:6px"><b>★★★★★</b>300reviews</div>
  <div class="buy" style="margin-top:12px"><span>−</span><span class="qty">1</span><span>+</span><span class="btn" style="width:135px;height:33px;line-height:33px;font-size:12px;margin-left:8px">Add to Card</span></div>
  <p class="copy" style="margin-top:20px">ta belle pièce is a leading Online Store. We provide an unparalleled selection of the very best quality products, an easy and comfortable shopping experience, expedited shipping offers, and exceptional customer service. Check out our collection of new arrivals, best sellers, and clearance items today.</p>
</article>
<div class="abs arrows" style="left:630px;top:2499px">
  <span class="prev"><svg width="10" height="14" viewBox="0 0 10 14"><path d="M8 1L2 7l6 6" stroke="#fff" stroke-width="2.5" fill="none"/></svg></span>
  <span class="next"><svg width="10" height="14" viewBox="0 0 10 14"><path d="M2 1l6 6-6 6" stroke="#fff" stroke-width="2.5" fill="none"/></svg></span>
</div>

<!-- Contact -->
<article class="abs" style="left:120px;top:2718px;width:460px">
  <h2 class="section-title">Contact</h2>
  <div class="title-rule"></div>
  <p class="lead" style="font-size:14px">For general comments and inquiries, please get in touch with us with the form below</p>
</article>
<div class="field" style="left:120px;top:2872px;width:220px;height:36px"></div>
<div class="field" style="left:356px;top:2872px;width:222px;height:36px">Email</div>
<div class="field" style="left:120px;top:2928px;width:458px;height:36px">Subject</div>
<div class="field" style="left:120px;top:2984px;width:458px;height:76px">Message</div>
<div class="abs btn" style="left:120px;top:3081px;width:458px;height:35px;line-height:35px">Send</div>
<div class="abs photo" style="left:630px;top:2669px;width:453px;height:498px;background:linear-gradient(180deg,#6a2a2a,#7c7a3a 30%,#8fc7cf 60%,#e889a0 80%,#9aa85a)" role="img" aria-label="Paint jars above a marbled sheet with pink flower patterns"></div>

<!-- Contact details -->
<section class="abs info-band">
  <div class="info" style="left:137px">
    <div class="circle"><svg width="30" height="40" viewBox="0 0 30 40"><path d="M15 1C7 1 1 7 1 15c0 10 14 24 14 24s14-14 14-24C29 7 23 1 15 1z" fill="#fff"/><circle cx="15" cy="15" r="5" fill="#d8322a"/></svg></div>
    <h4>ADRESS</h4><p>Dublin, Irelan</p>
  </div>
  <div class="info" style="left:480px">
    <div class="circle"><svg width="40" height="40" viewBox="0 0 24 24"><path d="M6.6 10.8a15 15 0 006.6 6.6l2.2-2.2a1 1 0 011-.25 11 11 0 003.5.56 1 1 0 011 1V20a1 1 0 01-1 1A17 17 0 013 4a1 1 0 011-1h3.5a1 1 0 011 1 11 11 0 00.56 3.5 1 1 0 01-.25 1z" fill="#fff"/></svg></div>
    <h4>PHONE</h4><p>08 555 014 372</p>
  </div>
  <div class="info" style="left:787px">
    <div class="circle"><svg width="40" height="30" viewBox="0 0 40 30"><rect x="1" y="1" width="38" height="28" fill="#fff"/><path d="M1 1l19 16L39 1" stroke="#d8322a" stroke-width="2.5" fill="none"/></svg></div>
    <h4>EMAIL</h4><p>info@tabellepiece.com</p>
  </div>
</section>

<section class="abs newsletter" aria-label="Newsletter">
  <h3>SUBSCRIBE TO OUR NEWSLETTER</h3>
  <h5>TO RECEIVE THE LATEST NEWS &amp; UPDATE</h5>
  <div class="subscribe"><span>Your E-Mail</span><b>SUBMIT</b></div>
</section>

<footer class="abs footer">PRIVACY POLICY - LEGAL MENTIONS - TERMS AND CONDITIONS
  <div class="social"><span></span><span></span><span></span><span></span><span></span></div>
</footer>

</body>
</html>
```